Tall Pines Restaurant & Cafe Marketing is a is a marketing company that specialises in Restaurant Marketing.
We show independent restaurant owners how to increase profits & beat their competition, we advise our customers on direct marketing methods that will help to make customers more loyal to their restaurant.
I have included some images of logos that I like the look off.
The final design should communicate that our business is professional and polished. I look forward to seeing your designs.
Restaurant

```html
<!DOCTYPE html>
<html lang="en">
<head>
<meta charset="utf-8">
<title>Tall Pines Restaurant Marketing – Business Cards</title>
<link href="https://fonts.googleapis.com/css2?family=Open+Sans:wght@400;600&display=swap" rel="stylesheet">
<style>
  :root {
    --page-bg: #d6d6d6;
    --card-dark: #1b1c1e;
    --card-dark-2: #2b2c2f;
    --card-light: #eceeef;
    --accent: #1ba6e3;
    --text-light: #e6e6e6;
  }
  * { box-sizing: border-box; margin: 0; padding: 0; }
  html, body {
    width: 1200px; height: 988px; overflow: hidden;
    background: var(--page-bg);
    font-family: "Open Sans", Arial, sans-serif;
  }
  .sheet {
    width: 1200px; height: 988px;
    display: flex; flex-direction: column; align-items: center; justify-content: center;
    gap: 60px;
  }
  .card {
    position: relative;
    width: 700px; height: 400px;
    overflow: hidden;
    box-shadow: 0 6px 18px rgba(0,0,0,0.25);
  }
  .card__band {
    position: absolute; left: 0; right: 0; height: 14px;
    background: var(--accent);
  }
  .card__band--top { top: 0; }
  .card__band--bottom { bottom: 0; }

  /* Back (dark) card */
  .card--back {
    background: linear-gradient(160deg, var(--card-dark-2), var(--card-dark) 60%);
  }
  .card__rule {
    position: absolute; left: 0; right: 0; height: 3px;
    background: var(--accent);
  }
  .card__rule--upper { top: 176px; }
  .card__rule--lower { top: 330px; }
  .wordmark {
    color: var(--accent);
    text-align: center;
    line-height: 1.15;
  }
  .card--back .wordmark {
    position: absolute; top: 62px; left: 0; right: 0;
  }
  .wordmark__name { font-size: 38px; font-weight: 400; }
  .wordmark__tagline { font-size: 26px; font-weight: 400; }

  .contact {
    position: absolute; top: 200px; left: 250px; right: 30px;
    display: grid; grid-template-columns: 1fr 1fr; row-gap: 14px; column-gap: 16px;
    list-style: none;
    color: var(--text-light); font-size: 13px;
  }
  .contact__item { display: flex; align-items: center; gap: 8px; white-space: nowrap; }
  .contact__item--wide { grid-column: 1 / span 2; }
  .contact__icon { width: 16px; height: 16px; flex: none; }

  .person {
    position: absolute; left: 36px; top: 282px;
    line-height: 1.3;
  }
  .person__name { color: var(--accent); font-size: 15px; font-weight: 600; letter-spacing: 0.5px; text-transform: uppercase; }
  .person__role { color: var(--text-light); font-size: 12px; letter-spacing: 0.5px; text-transform: uppercase; }

  /* Front (light) card */
  .card--front { background: var(--card-light); }
  .card--front .wordmark {
    position: absolute; top: 0; bottom: 0; left: 0; right: 0;
    display: flex; flex-direction: column; justify-content: center;
  }
  .card--front .wordmark__name { font-size: 46px; }
  .card--front .wordmark__tagline { font-size: 32px; }
</style>
</head>
<body>
<main class="sheet">

  <section class="card card--back" aria-label="Business card back">
    <div class="card__band card__band--top"></div>
    <div class="wordmark">
      <div class="wordmark__name">Tall Pines</div>
      <div class="wordmark__tagline">Restaurant Marketing</div>
    </div>
    <div class="card__rule card__rule--upper"></div>

    <ul class="contact">
      <li class="contact__item">
        <svg class="contact__icon" viewBox="0 0 16 16"><circle cx="8" cy="8" r="8" fill="#1ba6e3"/><path d="M5.5 4.5l1.5 0 .7 2-1 .8a5 5 0 0 0 2 2l.8-1 2 .7v1.5c0 .5-.5 1-1 1A7 7 0 0 1 4.5 5.5c0-.5.5-1 1-1z" fill="#fff"/></svg>
        020 555 0142
      </li>
      <li class="contact__item">
        <svg class="contact__icon" viewBox="0 0 16 16"><circle cx="8" cy="8" r="8" fill="#1ba6e3"/><path d="M5.5 4.5l1.5 0 .7 2-1 .8a5 5 0 0 0 2 2l.8-1 2 .7v1.5c0 .5-.5 1-1 1A7 7 0 0 1 4.5 5.5c0-.5.5-1 1-1z" fill="#fff"/></svg>
        020 555 0187
      </li>
      <li class="contact__item">
        <svg class="contact__icon" viewBox="0 0 16 16"><circle cx="8" cy="8" r="8" fill="#1ba6e3"/><rect x="4" y="5" width="8" height="6" fill="none" stroke="#fff" stroke-width="1"/><path d="M4 5l4 3.2L12 5" fill="none" stroke="#fff" stroke-width="1"/></svg>
        daniel@tallpines.com
      </li>
      <li class="contact__item">
        <svg class="contact__icon" viewBox="0 0 16 16"><circle cx="8" cy="8" r="8" fill="#1ba6e3"/><circle cx="8" cy="8" r="4" fill="none" stroke="#fff" stroke-width="1"/><path d="M4 8h8M8 4c-2 2.5-2 5.5 0 8M8 4c2 2.5 2 5.5 0 8" fill="none" stroke="#fff" stroke-width="0.9"/></svg>
        www.tallpinesmarketing.com
      </li>
      <li class="contact__item contact__item--wide">
        <svg class="contact__icon" viewBox="0 0 16 16"><circle cx="8" cy="8" r="8" fill="#1ba6e3"/><path d="M8 3.5a3 3 0 0 1 3 3c0 2.2-3 5.5-3 5.5S5 8.7 5 6.5a3 3 0 0 1 3-3z" fill="#fff"/><circle cx="8" cy="6.5" r="1" fill="#1ba6e3"/></svg>
        18 Cedar Lane, Pine Ridge Road, UK
      </li>
    </ul>

    <div class="person">
      <div class="person__name">Daniel Mercer</div>
      <div class="person__role">Financial Advisor</div>
    </div>
    <div class="card__rule card__rule--lower"></div>
    <div class="card__band card__band--bottom"></div>
  </section>

  <section class="card card--front" aria-label="Business card front">
    <div class="card__band card__band--top"></div>
    <div class="wordmark">
      <div class="wordmark__name">Tall Pines</div>
      <div class="wordmark__tagline">Restaurant Marketing</div>
    </div>
  </section>

</main>
</body>
</html>
```